Bella Visto Restaurant take out menu

We need a take out menu design that is trendy for a casual upscale Italian restaurant with a vast menu. This menu must be able to be 4 color and reproducible in large quantities to be bulked mailed or inserted into a daily paper. It must also maintain a theme that can be crossed over to our in house dining menu and specials menu.
OUR WEBSITE:
www.bellavistoplates.example
For the content, go to the Menu section of our website. We are interested in the design scheme and a template to use.
Target Market(s)
families, sinle individuals seeking take out meals and delivery
Industry/Entity Type
Restaurant
Look and feel
Each slider illustrates characteristics of the customer's brand and the style your logo design should communicate.

```html
<!DOCTYPE html>
<html lang="en">
<head>
<meta charset="utf-8">
<title>Bella Visto Italian Cuisine – Take Out Menu</title>
<link href="https://fonts.googleapis.com/css2?family=Playfair+Display:ital,wght@0,400;0,700;1,400;1,700&family=Roboto+Condensed:wght@400;700&display=swap" rel="stylesheet">
<style>
  :root{
    --cream:#f4e8d2;
    --wine:#8a1b12;
    --wine-dark:#7a1610;
    --wine-soft:#962a20;
    --ink:#6e1a12;
    --white:#fffaf1;
  }
  *{margin:0;padding:0;box-sizing:border-box}
  html,body{width:851px;height:1200px;overflow:hidden;background:var(--cream)}
  .menu{position:relative;width:851px;height:1200px;background:var(--cream);color:var(--ink);font-family:"Roboto Condensed",Arial,sans-serif}
  .backdrop{position:absolute;inset:0}
  .call{position:absolute;left:22px;top:14px;font-family:"Playfair Display",Georgia,serif}
  .call__label{font-size:22px;letter-spacing:1px;color:var(--wine)}
  .call__phone{font-size:42px;font-weight:700;color:var(--wine);line-height:1}
  .brand{position:absolute;left:440px;top:18px;width:395px;text-align:center;font-family:"Playfair Display",Georgia,serif;font-weight:700;color:var(--wine)}
  .brand__name{font-size:74px;line-height:1}
  .brand__tag{font-size:22px;letter-spacing:4px;margin-top:6px}
  .section-title{font-family:"Playfair Display",Georgia,serif;color:var(--wine);font-weight:400}
  .pizza{position:absolute;left:22px;top:118px;width:388px}
  .pizza .section-title{font-size:34px;text-align:center}
  .pizza__toppings{text-align:center;font-size:13px;margin-top:2px}
  .pizza__toppings-list{text-align:center;font-size:8.5px;text-transform:uppercase;line-height:1.35;margin:3px 0 10px}
  .item{display:flex;justify-content:space-between;align-items:baseline}
  .item__name{font-family:"Playfair Display",Georgia,serif;font-style:italic;font-weight:700;color:var(--wine)}
  .item__desc{font-size:10px;line-height:1.2;color:var(--ink)}
  .pizza .item__name{font-size:17px}
  .pizza .item__price{font-size:14px}
  .pizza__entry{height:49px}
  .burgers{position:absolute;left:22px;top:792px;width:330px}
  .burgers .section-title{font-size:34px}
  .burgers__intro{font-size:12px;text-transform:uppercase;line-height:1.2;margin:4px 0 8px}
  .burgers__entry{height:33px}
  .burgers .item{justify-content:flex-start;gap:8px}
  .burgers .item__name{font-size:15px}
  .burgers .item__price{font-size:14px}
  .subs{position:absolute;top:206px;color:var(--white)}
  .subs--hot{left:445px;width:190px}
  .subs--cold{left:660px;width:180px}
  .subs .section-title{color:var(--white);font-size:32px;line-height:1}
  .subs__note{font-size:14px;margin:4px 0 14px}
  .subs__list{list-style:none;font-size:14.5px;line-height:20px}
  .promo{position:absolute;left:650px;top:510px;width:195px;color:var(--white);font-family:"Playfair Display",Georgia,serif;font-weight:700;font-size:27px;line-height:1.15;text-align:center}
  .order-up{position:absolute;left:500px;top:975px;color:var(--white);font-family:"Playfair Display",Georgia,serif;font-weight:700;font-size:46px;letter-spacing:1px}
  .site{position:absolute;left:22px;top:1182px;font-size:11px;color:var(--wine)}
</style>
</head>
<body>
<main class="menu">
  <svg class="backdrop" width="851" height="1200" viewBox="0 0 851 1200" aria-hidden="true">
    <path d="M455 195 H851 V1175 H700 A290 290 0 0 1 380 900 A300 300 0 0 1 425 795 V225 A30 30 0 0 1 455 195 Z" fill="var(--wine)"/>
    <line x1="645" y1="215" x2="645" y2="660" stroke="var(--cream)" stroke-width="2"/>
  </svg>
  <svg style="position:absolute;left:705px;top:690px" width="115" height="495" viewBox="0 0 115 495" role="img" aria-label="Fork silhouette graphic">
    <rect x="0" y="0" width="115" height="495" rx="30" fill="var(--wine-soft)"/>
  </svg>

  <header class="call">
    <div class="call__label">CALL US AT:</div>
    <div class="call__phone">555-014-2290</div>
  </header>

  <div class="brand">
    <div class="brand__name">Bella Visto</div>
    <div class="brand__tag">ITALIAN CUISINE</div>
  </div>

  <section class="pizza">
    <h2 class="section-title">Bella Visto Pizza</h2>
    <p class="pizza__toppings">Toppings for 1.99</p>
    <p class="pizza__toppings-list">Ham · Broccoli · Extra Cheese · Pepperoni · Sausage · Peppers · Onions<br>Mushrooms · Olives · Spinach · Bacon · Tomato · Garlic · Anchovies</p>
    <div class="pizza__entry"><div class="item"><span class="item__name">Plain Cheese</span><span class="item__price">8.99/11.99/12.99</span></div></div>
    <div class="pizza__entry"><div class="item"><span class="item__name">Traditional White</span><span class="item__price">8.99/11.99/13.99</span></div><p class="item__desc">Olive oil, garlic, ricotta and mozzarella.</p></div>
    <div class="pizza__entry"><div class="item"><span class="item__name">Chicken Bacon Ranch</span><span class="item__price">10.99/14.99/16.99</span></div><p class="item__desc">Grilled chicken, bacon, ranch and mozzarella cheese.</p></div>
    <div class="pizza__entry"><div class="item"><span class="item__name">Buona Bambino</span><span class="item__price">10.99/14.99/16.99</span></div><p class="item__desc">Fresh basil, tomato, mozzarella and ricotta.</p></div>
    <div class="pizza__entry"><div class="item"><span class="item__name">Buffalo Chicken</span><span class="item__price">10.99/14.99/16.99</span></div><p class="item__desc">Buffalo sauce, chicken, mozzarella and blue cheese.</p></div>
    <div class="pizza__entry"><div class="item"><span class="item__name">Bella Visto Special</span><span class="item__price">12.99/16.99/18.99</span></div><p class="item__desc">Pepperoni, sausage, peppers, onions, mushrooms and olives.</p></div>
    <div class="pizza__entry"><div class="item"><span class="item__name">Margarita</span><span class="item__price">8.99/11.99/13.99</span></div><p class="item__desc">Fresh basil, tomato, fresh mozzarella and olive oil.</p></div>
    <div class="pizza__entry"><div class="item"><span class="item__name">Roasted Vegetable</span><span class="item__price">11.99/14.99/16.99</span></div><p class="item__desc">Eggplant, zucchini, peppers, onions and spinach.</p></div>
    <div class="pizza__entry"><div class="item"><span class="item__name">Sweet Hawaiian</span><span class="item__price">11.99/14.99/16.99</span></div><p class="item__desc">Pineapple, ham, bacon and mozzarella.</p></div>
    <div class="pizza__entry"><div class="item"><span class="item__name">Spinach and Artichoke</span><span class="item__price">11.99/14.99/16.99</span></div><p class="item__desc">Spinach, artichoke hearts, garlic and ricotta.</p></div>
    <div class="pizza__entry"><div class="item"><span class="item__name">Philly Cheese Steak</span><span class="item__price">8.99/11.99/12.99</span></div><p class="item__desc">Steak, onions, peppers and American cheese.</p></div>
    <div class="pizza__entry"><div class="item"><span class="item__name">Grandma's Pie</span><span class="item__price">14.99</span></div><p class="item__desc">Thin square crust, plum tomato and basil.</p></div>
  </section>

  <section class="burgers">
    <h2 class="section-title">Awesome Burgers</h2>
    <p class="burgers__intro">All certified black angus beef served on a kaiser roll with french fries and a fried pickle</p>
    <div class="burgers__entry"><div class="item"><span class="item__name">Cheeseburger</span><span class="item__price">7.99</span></div></div>
    <div class="burgers__entry"><div class="item"><span class="item__name">Bacon Cheddar</span></div><p class="item__desc">Applewood smoked bacon, sharp cheddar.</p></div>
    <div class="burgers__entry"><div class="item"><span class="item__name">Blue Cheese BLT</span></div><p class="item__desc">Bacon, lettuce, tomato and blue cheese. 9.59</p></div>
    <div class="burgers__entry"><div class="item"><span class="item__name">California</span></div><p class="item__desc">Avocado, roasted red pepper and pepper jack. 9.99</p></div>
    <div class="burgers__entry"><div class="item"><span class="item__name">Gourmet Sliders</span></div><p class="item__desc">Three mini burgers with American cheese. 8.99</p></div>
    <div class="burgers__entry"><div class="item"><span class="item__name">Mushroom Swiss</span><span class="item__price">8.59</span></div><p class="item__desc">Sautéed mushrooms and melted Swiss cheese.</p></div>
    <div class="burgers__entry"><div class="item"><span class="item__name">Portabella</span></div><p class="item__desc">Grilled portabella cap, roasted peppers, mozzarella. 8.59</p></div>
    <div class="burgers__entry"><div class="item"><span class="item__name">Pub</span></div><p class="item__desc">Fried onion, bacon, cheddar and pub sauce. 9.99</p></div>
    <div class="burgers__entry"><div class="item"><span class="item__name">Smokehouse Barbecue</span></div><p class="item__desc">Smoked bacon, cheddar, onion rings, barbecue sauce. 9.59</p></div>
  </section>

  <section class="subs subs--hot">
    <h2 class="section-title">Hot Subs</h2>
    <p class="subs__note">Add Cheese for $0.50</p>
    <ul class="subs__list">
      <li>Cheesesteak 6.99</li><li>Bacon Cheesesteak 7.59</li><li>Steak Sub 6.29</li><li>Chicken Parmigiana 6.99</li><li>Pepper, Egg, &amp; Cheese 6.29</li><li>Pizza Cheesesteak 6.99</li><li>Meatball Parmigiana 6.99</li><li>Mushroom Cheesesteak 6.99</li><li>Veal Parmigiana 7.99</li><li>Pepper Cheesesteak 6.99</li><li>Vegetarian with Cheese 6.59</li><li>Eggplant Parmigiana 6.59</li><li>Chicken Cheesesteak 6.99</li><li>Sausage Parmigiana 7.59</li><li>Grilled Chicken 6.59</li><li>Cheeseburger Sub 7.59</li><li>Steak Caesar 7.59</li><li>Sausage, Peppers &amp; Onion 6.99</li>
    </ul>
  </section>

  <section class="subs subs--cold">
    <h2 class="section-title">Cold Subs</h2>
    <p class="subs__note">Add Cheese for $0.50</p>
    <ul class="subs__list">
      <li>Regular Italian 6.59</li><li>Tuna 6.59</li><li>Roast Beef 7.59</li><li>Imported Ham 6.59</li><li>Roast Turkey 6.99</li><li>Provolone 6.59</li><li>Capicola, Salami, &amp; Provolone 6.59</li><li>Chicken Salad 6.99</li>
    </ul>
  </section>

  <p class="promo">Harborview's #1 Take Out, Pick Up or free delivery right to your door!</p>
  <p class="order-up">ORDER UP!</p>
  <p class="site">www.bellavistoplates.example</p>
</main>
</body>
</html>
```